Educational non-profit needs an End of the Year Flyer

We need a flyer to mail to our supporters asking for donations to our program. Hillcrest Open Learning Hub runs after school programs for low-income students in Pasadena, CA. This is our end of the year mailing to supporters asking them to finish out the year with their contributions so that we can meet our budget.

Target Market(s)

Donors and supporters of organization

Industry/Entity Type

Non-Profit

Font styles to use
Serif

Colors

Designer to choose colors to be used in the design.

Requirements
Must have
• The project should fit on a 6x9" card, and be printed on front and back. It should show pictures, use the copy I have included, a space for a label address, a stamp, and the return address.
Nice to have
• eye-catching, fun

```html
<!DOCTYPE html>
<html lang="en">
<head>
<meta charset="utf-8">
<title>Hillcrest Open Learning Hub – End of Year Mailer</title>
<link rel="stylesheet" href="https://fonts.googleapis.com/css2?family=Open+Sans:wght@400;600;700&family=Ultra&display=swap">
<style>
  :root{
    --bg:#e9e9e7;
    --paper:#ffffff;
    --yellow:#f6ec1f;
    --yellow-deep:#f2e31a;
    --ink:#1d1d1d;
    --ink-soft:#4a4a4a;
    --red:#e3262d;
    --line:#555555;
    --shadow:rgba(0,0,0,.28);
  }
  *{margin:0;padding:0;box-sizing:border-box}
  html,body{width:1200px;height:1000px;overflow:hidden}
  body{background:var(--bg);font-family:"Open Sans",Arial,sans-serif;color:var(--ink);position:relative}

  .card{position:absolute;width:654px;height:435px;background:var(--paper);box-shadow:3px 4px 8px var(--shadow);overflow:hidden}

  /* Back side */
  .card-back{left:111px;top:148px}
  .back-photo{position:absolute;left:0;top:0;width:332px;height:435px;
    background:linear-gradient(180deg,#2b2a2c 0%,#3b3635 38%,#6b4c45 58%,#b7a89b 72%,#7b6a5f 86%,#2f2b2a 100%)}
  .back-bar{position:absolute;left:332px;top:0;width:12px;height:435px;background:var(--yellow)}
  .return-address{position:absolute;left:358px;top:66px;font-size:10px;line-height:13px;color:var(--ink-soft);font-style:normal}
  .stamp-box{position:absolute;left:556px;top:32px;width:69px;height:66px;border:1.5px solid var(--ink)}
  .label-line{position:absolute;left:358px;width:267px;height:0;border-top:1px solid var(--line)}
  .label-line.one{top:242px}
  .label-line.two{top:272px}

  /* Front side */
  .card-front{left:437px;top:430px;width:653px}
  .front-art{position:absolute;inset:0}
  .logo-lockup{position:absolute;left:516px;top:40px;width:120px;display:flex;flex-direction:column;align-items:center;gap:6px;text-align:center}
  .logo-dot{width:26px;height:26px;border-radius:50%;background:var(--yellow)}
  .logo-name{font-size:10px;font-weight:600;line-height:12px;color:var(--ink)}

  .headline{position:absolute;left:365px;top:224px;width:215px;text-align:center;white-space:nowrap;
    font-family:"Ultra",Georgia,serif;font-weight:400;font-size:17px;line-height:24px;color:var(--red);
    text-shadow:-2px -2px 0 #fff,2px -2px 0 #fff,-2px 2px 0 #fff,2px 2px 0 #fff,0 2px 0 #fff,0 -2px 0 #fff,2px 0 0 #fff,-2px 0 0 #fff}

  .appeal{position:absolute;left:21px;top:228px;font-size:10.6px;line-height:14px;color:var(--ink);white-space:nowrap}
  .appeal-ask{position:absolute;left:21px;top:329px;font-size:13.6px;line-height:17px;font-weight:700;color:var(--ink);white-space:nowrap}
  .appeal-note{position:absolute;left:21px;top:367px;font-size:11.6px;line-height:15px;color:var(--ink);white-space:nowrap}
  .appeal-web{position:absolute;left:21px;top:390px;font-size:11.6px;line-height:15px;color:var(--ink);display:flex;align-items:center;gap:8px;white-space:nowrap}
  .web-pill{background:#fff;border-radius:9px;padding:1px 6px;font-size:11.4px}

  .divider{position:absolute;left:381px;top:322px;width:0;height:100px;border-left:1px solid var(--ink-soft)}
  .contact-list{position:absolute;left:395px;top:343px;list-style:none;font-size:9.6px;color:var(--ink-soft)}
  .contact-list li{display:flex;align-items:center;gap:8px;height:19px;white-space:nowrap}
  .contact-list svg{width:11px;height:11px;flex:none}
</style>
</head>
<body>

<section class="card card-back" aria-label="Mailer back side">
  <div class="back-photo" role="img" aria-label="Photo of a children's choir performing on a lit stage before an audience"></div>
  <div class="back-bar"></div>
  <address class="return-address">
    Hillcrest Open Learning Hub<br>
    218 W. Alder Lane<br>
    Pasadena, CA&nbsp; 91104
  </address>
  <div class="stamp-box" aria-label="Stamp area"></div>
  <div class="label-line one"></div>
  <div class="label-line two"></div>
</section>

<section class="card card-front" aria-label="Mailer front side">
  <svg class="front-art" width="653" height="435" viewBox="0 0 653 435">
    <defs>
      <linearGradient id="playground" x1="0" y1="0" x2="1" y2="1">
        <stop offset="0" stop-color="#e7c44a"/>
        <stop offset=".3" stop-color="#8fc3d6"/>
        <stop offset=".55" stop-color="#c9483d"/>
        <stop offset=".8" stop-color="#e2c39a"/>
        <stop offset="1" stop-color="#d9b983"/>
      </linearGradient>
      <linearGradient id="group" x1="0" y1="0" x2="0" y2="1">
        <stop offset="0" stop-color="#6d6a66"/>
        <stop offset=".5" stop-color="#3a3e4f"/>
        <stop offset="1" stop-color="#8c7b74"/>
      </linearGradient>
    </defs>
    <rect width="653" height="435" fill="url(#playground)" role="img" aria-label="Photo of a smiling boy at a colorful playground"/>
    <path d="M0,150 C90,185 170,200 250,230 C320,256 360,300 395,345 C470,333 560,318 653,288 L653,435 L0,435 Z" fill="var(--yellow)"/>
    <circle cx="111" cy="90" r="96" fill="url(#group)" stroke="var(--yellow-deep)" stroke-width="6" role="img" aria-label="Photo of a group of program children"/>
    <ellipse cx="640" cy="10" rx="172" ry="140" fill="var(--paper)"/>
  </svg>

  <div class="logo-lockup">
    <span class="logo-dot"></span>
    <span class="logo-name">Hillcrest Open Learning Hub</span>
  </div>

  <h1 class="headline">WE NEED YOUR HELP<br>TO FINISH OUT 2018<br>STRONG!</h1>

  <p class="appeal">We have had a wonderful 25th year of<br>serving the children and families of Pasadena here<br>at Hillcrest Open Learning Hub with high<br>quality afterschool programs.&nbsp; Hundreds and hundreds of<br>students have been a part of the Bright Step Kids Club family.&nbsp; Our<br>annual budget is $275,000 and we count on $100,000 from<br>individual donors.</p>
  <p class="appeal-ask">WILL YOU JOIN WITH US FOR AN END OF<br>THE YEAR CONTRIBUTION?</p>
  <p class="appeal-note">Remember, you can give online through PayWell.</p>
  <p class="appeal-web">Just look for the link on our website <span class="web-pill">www.brightstepkids.org</span></p>

  <div class="divider"></div>
  <ul class="contact-list">
    <li><svg viewBox="0 0 12 12"><path d="M3 1 L5 3.5 L4 5 C4.8 6.6 5.6 7.4 7 8 L8.5 7 L11 9 L9.8 11 C5 10.5 1.5 7 1 2.2 Z" fill="var(--ink)"/></svg>(626) 555-0148</li>
    <li><svg viewBox="0 0 12 12"><path d="M6 0.5 C3.6 0.5 2 2.3 2 4.4 C2 7 6 11.5 6 11.5 C6 11.5 10 7 10 4.4 C10 2.3 8.4 0.5 6 0.5 Z" fill="var(--ink)"/><circle cx="6" cy="4.4" r="1.5" fill="var(--yellow)"/></svg>218 W. Alder Lane, Pasadena, CA 91104</li>
    <li><svg viewBox="0 0 12 12"><rect x="0.8" y="2.5" width="10.4" height="7" fill="none" stroke="var(--ink)" stroke-width="1"/><path d="M1 3 L6 6.8 L11 3" fill="none" stroke="var(--ink)" stroke-width="1"/></svg>hello@brightstepkids.org</li>
    <li><svg viewBox="0 0 12 12"><circle cx="6" cy="6" r="5" fill="none" stroke="var(--ink)" stroke-width="1"/></svg>Hillcrest Open Learning Hub</li>
  </ul>
</section>

</body>
</html>
```